Custom unique Stationary design for Logistics company

We need a custom, unique , elegant and luxurious full stationary design using our new logo, following these guidelines:
1- Business card: double sided, both sides uses the navy blue as the background main color (same as the code of the navy blue used in our logo).
2- envelope and folder: also use the same navy blue as the main background color.
3- book cover( notepad cover) : same thing with the navy blue
4- letterhead: feel free to use the combination of the colors in our logo.
5- rest of the items are up to your creativity

Target Market(s)

corporates and other businesses

Industry/Entity Type

Logistics and heavy machines contractors

Requirements
Must have
• Letterhead, business card, envelope, notepad cover, paper, file
Nice to have
• navy blue to be main background color for business card, envelope, notepad cover

```html
<!DOCTYPE html>
<html lang="en">
<head>
<meta charset="utf-8">
<title>Meridian Freight Group – Presentation Folder</title>
<link rel="stylesheet" href="https://fonts.googleapis.com/css2?family=Montserrat:wght@400;600;800&display=swap">
<style>
  :root {
    --navy: #0c4a6e;
    --navy-deep: #08344f;
    --orange: #e0622e;
    --orange-deep: #c24e22;
    --paper: #ffffff;
    --ink-grey: #8a8d91;
    --backdrop: #d9d9da;
    --contact-text: #9fb8c9;
  }
  * { margin: 0; padding: 0; box-sizing: border-box; }
  html, body {
    width: 1200px;
    height: 847px;
    overflow: hidden;
    background: var(--backdrop);
    font-family: "Montserrat", sans-serif;
  }
  .canvas {
    position: relative;
    width: 1200px;
    height: 847px;
    display: flex;
    justify-content: center;
    align-items: center;
  }
  .folder {
    display: flex;
    width: 840px;
    height: 594px;
    box-shadow: 0 18px 40px rgba(0, 0, 0, 0.22);
  }
  .folder-back {
    position: relative;
    width: 420px;
    height: 100%;
    background: linear-gradient(90deg, var(--navy-deep) 0%, var(--navy) 50%, var(--navy-deep) 100%);
  }
  .contact-block {
    position: absolute;
    left: 0;
    right: 0;
    bottom: 62px;
    text-align: center;
    color: var(--contact-text);
    font-size: 8.5px;
    line-height: 1.55;
    letter-spacing: 0.3px;
  }
  .contact-block .contact-line { display: block; }
  .contact-block .inline-icon {
    display: inline-block;
    vertical-align: -1px;
    margin: 0 3px 0 6px;
  }
  .folder-front {
    position: relative;
    width: 420px;
    height: 100%;
    background: var(--paper);
  }
  .brand {
    position: absolute;
    top: 228px;
    left: 0;
    right: 0;
    display: flex;
    justify-content: center;
    align-items: center;
    gap: 10px;
  }
  .brand-dot {
    width: 12px;
    height: 12px;
    border-radius: 50%;
    background: var(--orange);
  }
  .brand-name {
    color: var(--navy);
    font-weight: 800;
    font-size: 22px;
    letter-spacing: 1.5px;
    text-transform: uppercase;
  }
  .footer-bands {
    position: absolute;
    left: 0;
    right: 0;
    bottom: 42px;
    height: 26px;
  }
  .web-band {
    position: absolute;
    left: 0;
    top: 6px;
    width: 320px;
    height: 14px;
    background: var(--navy);
    clip-path: polygon(0 0, 100% 0, 97% 100%, 0 100%);
  }
  .accent-band {
    position: absolute;
    right: 0;
    top: 0;
    width: 96px;
    height: 14px;
    background: var(--orange-deep);
    clip-path: polygon(6% 0, 100% 0, 100% 100%, 0 100%);
  }
  .web-address {
    position: absolute;
    right: 112px;
    top: 22px;
    color: var(--navy);
    font-weight: 800;
    font-size: 8px;
    letter-spacing: 1px;
    text-transform: uppercase;
  }
</style>
</head>
<body>
<main class="canvas">
  <section class="folder" aria-label="Presentation folder, open flat">
    <div class="folder-back">
      <address class="contact-block" style="font-style: normal;">
        <span class="contact-line">Meridian Freight Group</span>
        <span class="contact-line">48 Harbour Crest Road, Oakridge, ON L7K 3P2</span>
        <span class="contact-line">
          <svg class="inline-icon" width="8" height="8" viewBox="0 0 24 24" aria-hidden="true"><path fill="#e0622e" d="M6.6 10.8a15.1 15.1 0 0 0 6.6 6.6l2.2-2.2a1 1 0 0 1 1-.25 11.4 11.4 0 0 0 3.6.57 1 1 0 0 1 1 1V20a1 1 0 0 1-1 1A17 17 0 0 1 3 4a1 1 0 0 1 1-1h3.5a1 1 0 0 1 1 1c0 1.25.2 2.45.57 3.57a1 1 0 0 1-.25 1z"/></svg>+15550142789
          <svg class="inline-icon" width="9" height="7" viewBox="0 0 24 18" aria-hidden="true"><rect width="24" height="18" rx="2" fill="#e0622e"/><path d="M2 2l10 8 10-8" stroke="#0c4a6e" stroke-width="2" fill="none"/></svg>hello@meridianfreight.com
        </span>
        <span class="contact-line">www.meridianfreight.com</span>
      </address>
    </div>
    <div class="folder-front">
      <div class="brand">
        <span class="brand-dot" aria-hidden="true"></span>
        <span class="brand-name">Meridian Freight Group</span>
      </div>
      <div class="footer-bands" aria-hidden="true">
        <div class="web-band"></div>
        <div class="accent-band"></div>
      </div>
      <p class="web-address">www.meridianfreight.com</p>
    </div>
  </section>
</main>
</body>
</html>
```